Jewelry Business card for general purpose. Elegant and simple

We are a jewelry group with 6 stores in Mexico and 30 years in business.

We need a BC that at leats includes the name, mail, phone number and physical location (street, municipality, and county; example "Paseo Olmeda 2140", "Avenida Sotillo", "Monterrey").
Optional: we are trying to reposition the brand with the association of life-events or moments and family. Such as: birth, marriage, graduation, birthdays. Christmast, mothers day and fathers day.

We are looking for something elegant but simple

Jewelry name: "Lunetti". Email: "lunettibrillo@correo-ejemplo.mx". Phone num "4172-3095".

Target Market(s)

General business card: from suppliers to clients. One segment outstand: couples gettineg married

Industry/Entity Type

Jewelry Store

Contact Information for Business Card

Loking for something simple but elegant.

Font styles to use
Decorative
Script

Requirements
Must have
• Must have name, address, and mail.
Nice to have
• It could have jewelry pictures/design. Maybe quotes. Or general words as background . currently we have a very simple card with one ring would like to see something different.
Should not have
• Include real people.

```html
<!DOCTYPE html>
<html lang="es">
<head>
<meta charset="utf-8">
<title>Lunetti Jewelry – Business Card</title>
<link href="https://fonts.googleapis.com/css2?family=Open+Sans:wght@400;600&display=swap" rel="stylesheet">
<style>
  :root {
    --page-bg: #d9d9d9;
    --card-black: #050505;
    --card-charcoal: #2a2a2a;
    --text-white: #f4f4f4;
    --text-soft: #cfcfcf;
    --gem-light: #e9ecf2;
    --gem-mid: #8f939c;
    --gem-dark: #1b1c20;
    --sparkle: #b9c4ff;
  }
  * { margin: 0; padding: 0; box-sizing: border-box; }
  html, body {
    width: 1200px; height: 1023px; overflow: hidden;
    background: var(--page-bg);
    font-family: "Open Sans", Arial, sans-serif;
  }
  .stage {
    position: relative; width: 1200px; height: 1023px;
    display: flex; align-items: center; justify-content: center;
  }
  .card {
    position: relative; width: 900px; height: 514px;
    background: linear-gradient(160deg, var(--card-charcoal) 0%, var(--card-black) 55%, #000 100%);
    border-radius: 4px; overflow: hidden;
    box-shadow: 0 18px 40px rgba(0,0,0,.35);
  }
  .gem-photo {
    position: absolute; right: -40px; top: -30px; width: 400px; height: 574px;
    background: radial-gradient(ellipse at 50% 50%, var(--gem-light) 0%, var(--gem-mid) 38%, var(--gem-dark) 70%, var(--card-black) 100%);
    clip-path: polygon(22% 0, 100% 0, 100% 100%, 22% 100%, 0 50%);
  }
  .gem-faint {
    position: absolute; left: 330px; top: 350px; width: 110px; height: 70px;
    border-radius: 50%;
    background: radial-gradient(ellipse, rgba(220,224,232,.22), rgba(120,124,132,.08) 70%, transparent);
  }
  .streaks { position: absolute; inset: 0; }
  .brand {
    position: absolute; left: 70px; top: 120px;
    color: var(--text-white);
  }
  .brand-name { font-size: 58px; font-weight: 600; line-height: 1; letter-spacing: 1px; }
  .brand-sub { font-size: 20px; font-weight: 400; margin-left: 150px; margin-top: 2px; color: var(--text-soft); }
  .contact {
    position: absolute; left: 90px; top: 250px;
    list-style: none; color: var(--text-white);
  }
  .contact li {
    display: flex; align-items: flex-start; gap: 22px;
    font-size: 22px; line-height: 1.3; margin-bottom: 22px;
  }
  .contact svg { flex: none; width: 26px; height: 26px; margin-top: 2px; }
  .address span { display: block; }
</style>
</head>
<body>
<main class="stage">
  <article class="card">
    <div class="gem-photo" role="img" aria-label="Close-up photograph of a brilliant-cut diamond with sparkling facets"></div>
    <div class="gem-faint" role="img" aria-label="Faint small diamond photograph behind the address"></div>
    <svg class="streaks" viewBox="0 0 900 514" aria-hidden="true">
      <line x1="0" y1="505" x2="520" y2="450" stroke="#6a6a6a" stroke-width="2"/>
      <line x1="90" y1="514" x2="560" y2="470" stroke="#3c3c3c" stroke-width="1.5"/>
      <g stroke="var(--sparkle)" stroke-width="1.5" opacity=".8">
        <line x1="515" y1="215" x2="555" y2="215"/><line x1="535" y1="195" x2="535" y2="235"/>
      </g>
    </svg>
    <div class="brand">
      <div class="brand-name">Lunetti</div>
      <div class="brand-sub">Jewelry</div>
    </div>
    <ul class="contact">
      <li>
        <svg viewBox="0 0 24 24" aria-hidden="true"><path fill="#fff" d="M6.6 10.8a15 15 0 006.6 6.6l2.2-2.2a1 1 0 011-.25 11.4 11.4 0 003.6.6 1 1 0 011 1V20a1 1 0 01-1 1A17 17 0 013 4a1 1 0 011-1h3.5a1 1 0 011 1 11.4 11.4 0 00.6 3.6 1 1 0 01-.25 1z"/></svg>
        <span>4172-3095</span>
      </li>
      <li>
        <svg viewBox="0 0 24 24" aria-hidden="true"><rect x="2" y="5" width="20" height="14" fill="#fff"/><path d="M2 5l10 8 10-8" fill="none" stroke="#000" stroke-width="1.5"/></svg>
        <span>lunettibrillo@correo-ejemplo.mx</span>
      </li>
      <li class="address">
        <svg viewBox="0 0 24 24" aria-hidden="true"><path fill="#fff" d="M12 2a7 7 0 00-7 7c0 5 7 13 7 13s7-8 7-13a7 7 0 00-7-7zm0 9.5A2.5 2.5 0 1112 6.5a2.5 2.5 0 010 5z"/></svg>
        <div><span>Paseo Olmeda No. 2140</span><span>local 6 - Avenida Sotillo</span></div>
      </li>
    </ul>
  </article>
</main>
</body>
</html>
```